nonprofit organization looking for sleek new design

We need a fresh new look for this nonprofit organization, Harbor Lights Family Works, INC (HALIF, Inc.). This organization provides educational, nutritional, dental health, and specialized services to Tidewell children, aiming to support families meeting federal income poverty guidelines. Our mission is clear: "Creating a brighter future for the children and la familia." We focus on child development, family wellness, staff growth, and community partnerships.

```html
<!DOCTYPE html>
<html lang="en">
<head>
<meta charset="utf-8">
<title>Harbor Lights Family Works, INC</title>
<link href="https://fonts.googleapis.com/css2?family=Roboto:wght@400;500;700&family=Kaushan+Script&display=swap" rel="stylesheet">
<style>
:root{
  --orange:#de8a0c;
  --dark:#222222;
  --ink:#2b2b2b;
  --muted:#555555;
  --mist:#efefef;
  --white:#ffffff;
  --line:#9a9a9a;
}
*{box-sizing:border-box;margin:0;padding:0}
html,body{width:1200px;height:3625px;overflow:hidden}
body{position:relative;background:var(--white);font-family:'Roboto',sans-serif;color:var(--ink)}
.abs{position:absolute}
.btn{position:absolute;background:var(--orange);color:var(--white);border-radius:40px;display:flex;align-items:center;justify-content:center;font-size:13px}
.photo{position:absolute;background:linear-gradient(135deg,#9a9a9a,#4a4a4a)}
.section-title{position:absolute;left:0;width:1200px;text-align:center;font-weight:700;font-size:33px;color:var(--dark)}
.dash{position:absolute;height:3px;background:repeating-linear-gradient(90deg,var(--orange) 0 11px,transparent 11px 18px)}
.edge{position:absolute;left:0;width:1200px;height:14px}

/* nav */
.brand{left:121px;top:10px;font-size:30px;font-weight:700;color:var(--orange)}
.nav a{position:absolute;top:24px;font-size:11.5px;color:var(--ink);text-decoration:none}
.nav a.active{color:var(--orange)}

/* hero */
.hero-photo{left:0;top:63px;width:1200px;height:710px;background:linear-gradient(90deg,#3e3e3e 0%,#5a5a5a 35%,#8b8b8b 60%,#6c6c6c 100%)}
.welcome{left:110px;top:252px;font-family:'Kaushan Script',cursive;color:var(--orange);font-size:28px}
.hero-title{left:110px;top:294px;font-size:50px;font-weight:700;color:var(--white)}
.hero-text{left:112px;top:373px;width:530px;font-size:13px;line-height:21px;color:var(--white)}

.signup{left:204px;top:695px;width:794px;height:152px;background:var(--white);border-radius:16px;box-shadow:0 2px 10px rgba(0,0,0,.06)}
.signup h2{position:absolute;top:28px;width:100%;text-align:center;font-weight:400;font-size:22px;color:var(--dark)}
.field{position:absolute;height:38px;border:1.5px solid var(--line);border-radius:30px;font-size:9px;color:#555;padding-left:22px;display:flex;align-items:center;background:var(--white)}

/* about */
.band-mist{left:0;width:1200px;background:var(--mist)}
.h2{position:absolute;font-weight:700;font-size:33px;color:var(--dark)}
.para{position:absolute;font-size:12.5px;line-height:23.7px;color:#3a3a3a}
.ring{position:absolute;border-radius:50%;border:4px solid var(--white);box-shadow:0 0 0 1.5px #cfcfcf;background:linear-gradient(160deg,#a5a5a5,#3f3f3f)}

/* services */
.service{position:absolute;top:1548px;width:191px;height:300px;border-radius:96px;}
.service.orange{background:var(--orange)}
.service.dark{background:var(--dark)}
.service .pic{position:absolute;left:9px;top:12px;width:173px;height:173px;border-radius:50%;background:linear-gradient(160deg,#d5d5d5,#6f6f6f)}
.service span{position:absolute;top:212px;width:100%;text-align:center;color:var(--white);font-size:22px}
.arrow{position:absolute;width:44px;height:44px;border-radius:50%;border:1.3px solid #333;background:var(--white)}

/* events */
.event{position:absolute;top:2115px;width:285px;height:316px;border-radius:14px;color:var(--white)}
.event.orange{background:var(--orange)}
.event.dark{background:var(--dark)}
.event .pic{position:absolute;left:8px;top:8px;width:269px;height:175px;border-radius:12px;background:linear-gradient(160deg,#bdbdbd,#3d3d3d)}
.event h3{position:absolute;left:12px;top:198px;width:265px;font-size:18px;line-height:22px;font-weight:500}
.event .date{position:absolute;left:12px;top:246px;font-size:10.5px}
.event p{position:absolute;left:12px;top:265px;width:240px;font-size:10.5px;line-height:15px}

/* partners */
.partner{position:absolute;top:3118px;height:36px;background:#bdbdbd;border-radius:6px}

/* newsletter & footer */
.footer{left:0;top:3297px;width:1200px;height:328px;background:var(--dark)}
.news{left:203px;top:3221px;width:793px;height:170px;background:var(--mist);border-radius:16px}
.news h2{position:absolute;top:36px;width:100%;text-align:center;font-size:32px;font-weight:700;color:var(--dark)}
.fcol{position:absolute;top:3442px;color:var(--white);font-size:11px}
.fcol h4{color:var(--orange);font-weight:500;font-size:14px;margin-bottom:8px}
.fcol .row{display:flex;align-items:center;gap:8px;height:26px}
.fcol .dot{width:16px;height:16px;border-radius:50%;background:var(--orange);display:flex;align-items:center;justify-content:center}
.fcol .line{height:19px}
.rule{left:0;top:3575px;width:1200px;height:1px;background:#555}
.copy{left:0;top:3593px;width:1200px;text-align:center;color:var(--white);font-size:9px}
</style>
</head>
<body>

<svg width="0" height="0" class="abs">
  <defs>
    <pattern id="rag-white" width="24" height="14" patternUnits="userSpaceOnUse"><path d="M0 0H24V7L21 4L18 9L14 3L11 8L7 2L4 9L0 5Z" fill="#ffffff"/></pattern>
    <pattern id="rag-mist" width="24" height="14" patternUnits="userSpaceOnUse"><path d="M0 14V6L4 9L7 3L11 7L14 2L18 8L21 4L24 7V14Z" fill="#efefef"/></pattern>
    <pattern id="rag-mist-down" width="24" height="14" patternUnits="userSpaceOnUse"><path d="M0 0H24V7L21 4L18 9L14 3L11 8L7 2L4 9L0 5Z" fill="#efefef"/></pattern>
    <pattern id="rag-dark" width="24" height="14" patternUnits="userSpaceOnUse"><path d="M0 14V6L4 9L7 3L11 7L14 2L18 8L21 4L24 7V14Z" fill="#222222"/></pattern>
  </defs>
</svg>

<!-- header -->
<header class="nav">
  <div class="abs brand">HALIF, Inc.</div>
  <a class="active" style="left:363px">Home</a>
  <a style="left:443px">About Us</a>
  <a style="left:539px">Services</a>
  <a style="left:633px">What we do</a>
  <a style="left:733px">Events</a>
  <a style="left:815px">Blog</a>
  <div class="btn" style="left:978px;top:17px;width:100px;height:32px;font-size:11px">Contact Us</div>
</header>

<!-- hero -->
<section>
  <div class="abs hero-photo" role="img" aria-label="Black and white photograph of a young child looking at the camera"></div>
  <svg class="edge" style="top:63px"><rect width="1200" height="14" fill="url(#rag-white)"/></svg>
  <div class="abs band-mist" style="top:771px;height:590px"></div>
  <svg class="edge" style="top:758px"><rect width="1200" height="14" fill="url(#rag-mist)"/></svg>
  <div class="abs welcome">Welcome to</div>
  <h1 class="abs hero-title">Nonprofit organization</h1>
  <p class="abs hero-text">Lorem Ipsum is simply dummy text of the printing and typesetting industry. Lorem Ipsum has been the industry's standard dummy text ever since the 1500s, when an unknown printer took a galley of type and scrambled it to make a type specimen book. It has survived not only five centuries.</p>
  <div class="btn" style="left:113px;top:483px;width:171px;height:53px;font-size:15px">Get Started</div>

  <div class="abs signup">
    <h2>Never miss a chance to make a difference</h2>
    <div class="field" style="left:31px;top:73px;width:295px">Name:</div>
    <div class="field" style="left:336px;top:73px;width:296px">Email:</div>
    <div class="btn" style="left:642px;top:73px;width:119px;height:38px">Submit</div>
  </div>
</section>

<!-- about -->
<section>
  <h2 class="h2" style="left:184px;top:962px">About Us</h2>
  <div class="dash" style="left:184px;top:1003px;width:138px"></div>
  <p class="para" style="left:184px;top:1020px;width:360px">Lorem Ipsum is simply dummy text of the printing and typesetting industry. Lorem Ipsum has been the industry's standard dummy text ever since the 1500s, when an unknown printer took a galley of type and scrambled it to make a type specimen book. It has survived not only five centuries, but also the leap into electronic typesetting, remaining essentially unchanged.</p>
  <div class="btn" style="left:184px;top:1206px;width:118px;height:36px">Learn More</div>
  <div class="ring" style="left:643px;top:912px;width:374px;height:374px" role="img" aria-label="Photograph of three children standing close together"></div>
  <div class="ring" style="left:569px;top:1119px;width:168px;height:168px" role="img" aria-label="Photograph of two smiling children"></div>
</section>

<!-- services -->
<section>
  <svg class="edge" style="top:1350px"><rect width="1200" height="14" fill="url(#rag-white)"/></svg>
  <h2 class="section-title" style="top:1416px">Organization Provides</h2>
  <div class="dash" style="left:435px;top:1460px;width:330px"></div>
  <p class="abs" style="left:0;top:1491px;width:1200px;text-align:center;font-size:12.5px;line-height:19px;color:#333">Lorem Ipsum is simply dummy text of the printing and typesetting industry. Lorem Ipsum has been the industry's<br>standard dummy text ever since the 1500s,</p>

  <div class="arrow" style="left:48px;top:1659px"><svg width="44" height="44"><path d="M24 16L18 22L24 28" fill="none" stroke="#333" stroke-width="1.5"/></svg></div>
  <div class="arrow" style="left:1107px;top:1659px"><svg width="44" height="44"><path d="M20 16L26 22L20 28" fill="none" stroke="#333" stroke-width="1.5"/></svg></div>

  <div class="service orange" style="left:184px"><div class="pic" role="img" aria-label="Photograph of a child studying at a desk"></div><span>Educational</span></div>
  <div class="service dark" style="left:401px"><div class="pic" role="img" aria-label="Photograph of a child drinking from a cup"></div><span>Nutritional</span></div>
  <div class="service orange" style="left:619px"><div class="pic" role="img" aria-label="Photograph of a smiling child at a dental check-up"></div><span>Dental health</span></div>
  <div class="service dark" style="left:833px"><div class="pic" role="img" aria-label="Photograph of a group of children with raised hands"></div><span>Family wellness</span></div>
</section>

<!-- events -->
<section>
  <div class="abs band-mist" style="top:1906px;height:630px"></div>
  <svg class="edge" style="top:1893px"><rect width="1200" height="14" fill="url(#rag-mist)"/></svg>
  <h2 class="section-title" style="top:1993px">Latest Events</h2>
  <div class="dash" style="left:491px;top:2038px;width:218px"></div>

  <div class="arrow" style="left:48px;top:2242px"><svg width="44" height="44"><path d="M24 16L18 22L24 28" fill="none" stroke="#333" stroke-width="1.5"/></svg></div>
  <div class="arrow" style="left:1107px;top:2242px"><svg width="44" height="44"><path d="M20 16L26 22L20 28" fill="none" stroke="#333" stroke-width="1.5"/></svg></div>

  <article class="event orange" style="left:158px">
    <div class="pic" role="img" aria-label="Photograph of children standing by a shelter"></div>
    <h3>Lorem Ipsum is simply dummy text of the printing and</h3>
    <div class="date">April 15 – April 20, 2023</div>
    <p>Lorem Ipsum is simply dummy text of the printing and typesetting industry.</p>
  </article>
  <article class="event dark" style="left:456px">
    <div class="pic" role="img" aria-label="Photograph of a narrow village lane"></div>
    <h3>Lorem Ipsum is simply dummy text of the printing and</h3>
    <div class="date">April 15 – April 20, 2023</div>
    <p>Lorem Ipsum is simply dummy text of the printing and typesetting industry.</p>
  </article>
  <article class="event orange" style="left:756px">
    <div class="pic" role="img" aria-label="Photograph of two young siblings"></div>
    <h3>Lorem Ipsum is simply dummy text of the printing and</h3>
    <div class="date">April 15 – April 20, 2023</div>
    <p>Lorem Ipsum is simply dummy text of the printing and typesetting industry.</p>
  </article>
  <svg class="edge" style="top:2533px"><rect width="1200" height="14" fill="url(#rag-mist-down)"/></svg>
</section>

<!-- join -->
<section>
  <div class="ring" style="left:186px;top:2603px;width:374px;height:374px" role="img" aria-label="Photograph of children smiling at a window"></div>
  <div class="ring" style="left:461px;top:2801px;width:172px;height:172px" role="img" aria-label="Photograph of a smiling girl"></div>
  <h2 class="h2" style="left:675px;top:2651px">Join Us</h2>
  <div class="dash" style="left:675px;top:2692px;width:120px"></div>
  <p class="para" style="left:675px;top:2709px;width:355px">Lorem Ipsum is simply dummy text of the printing and typesetting industry. Lorem Ipsum has been the industry's standard dummy text ever since the 1500s, when an unknown printer took a galley of type and scrambled it to make a type specimen book. It has survived not only five centuries, but also the leap into electronic typesetting, remaining essentially unchanged.</p>
  <div class="btn" style="left:675px;top:2894px;width:119px;height:35px">Join Us</div>
</section>

<!-- partners -->
<section>
  <h2 class="section-title" style="top:3037px">Our Partners</h2>
  <div class="dash" style="left:498px;top:3082px;width:200px"></div>
  <div class="partner" style="left:128px;width:64px;border-radius:50%;height:44px;top:3113px"></div>
  <div class="partner" style="left:277px;width:135px"></div>
  <div class="partner" style="left:478px;width:152px"></div>
  <div class="partner" style="left:713px;width:133px"></div>
  <div class="partner" style="left:902px;width:186px"></div>
</section>

<!-- newsletter & footer -->
<footer>
  <div class="abs footer"></div>
  <svg class="edge" style="top:3284px"><rect width="1200" height="14" fill="url(#rag-dark)"/></svg>
  <div class="abs news">
    <h2>Subscribe Your Newsletter</h2>
    <div class="field" style="left:62px;top:92px;width:544px">Email:</div>
    <div class="btn" style="left:613px;top:92px;width:117px;height:38px">Subscribe</div>
  </div>

  <div class="fcol" style="left:121px;width:180px">
    <h4>HALIF, Inc.</h4>
    <p style="font-size:9px;line-height:15px">Lorem Ipsum is simply dummy text of the printing and typesetting industry. Lorem Ipsum has been the industry's standard dummy text</p>
  </div>
  <div class="fcol" style="left:370px">
    <h4>MENU</h4>
    <div class="line">About Us</div>
    <div class="line">Location</div>
    <div class="line">Amenities</div>
    <div class="line">Photo Gallery</div>
  </div>
  <div class="fcol" style="left:566px">
    <h4>CONTACT US</h4>
    <div class="row"><span class="dot"><svg width="10" height="10"><path d="M2 1L4 1L5 3.5L3.8 4.5Q5 6.5 6 6.8L7 5.5L9 6.5V8.5Q4 9 1.5 3Z" fill="#fff"/></svg></span>555 0142 736</div>
    <div class="row"><span class="dot"><svg width="10" height="10"><path d="M5 9.5L2 5A3 3 0 1 1 8 5Z" fill="#fff"/><circle cx="5" cy="4" r="1.2" fill="#de8a0c"/></svg></span>Lorem Ipsum is simply dummy</div>
    <div class="row"><span class="dot"><svg width="10" height="10"><rect x="1" y="2.5" width="8" height="5.5" fill="#fff"/><path d="M1 2.5L5 5.5L9 2.5" fill="none" stroke="#de8a0c" stroke-width="0.8"/></svg></span>hello@harborlightsfw.org</div>
  </div>
  <div class="fcol" style="left:871px">
    <h4>FOLLOW US</h4>
    <div class="row" style="height:25px"><span class="dot"></span>Wavecast</div>
    <div class="row" style="height:25px"><span class="dot"></span>ReelHub</div>
    <div class="row" style="height:25px"><span class="dot"></span>Snapwell</div>
    <div class="row" style="height:25px"><span class="dot"></span>Chirpline</div>
  </div>
  <div class="abs rule"></div>
  <div class="abs copy">Copyright © 2010-2024 nonprofit organization S.L. All rights reserved.</div>
</footer>

</body>
</html>
```